Criação de Papelaria Profissional para Associações, ONGs ou Comunidades
" Somos uma Associação Comercial, onde emitimos vários documentos aos nossos associados e o principal documento é o Certificado de Origem "

```html
<!DOCTYPE html>
<html lang="pt-BR">
<head>
<meta charset="UTF-8">
<title>AVECOM — Papel Timbrado</title>
<link rel="stylesheet" href="https://fonts.googleapis.com/css2?family=Montserrat:wght@500;700&family=Tinos&display=swap">
<style>
  :root {
    --canvas-bg: #e9eaec;
    --paper: #ffffff;
    --brand-blue: #1b5fa8;
    --text-dark: #1f1f1f;
    --text-muted: #8a8f96;
    --pattern-soft: #eaf1f8;
    --pattern-mid: #dbe7f2;
  }
  * { margin: 0; padding: 0; box-sizing: border-box; }
  html, body { width: 1200px; height: 1200px; overflow: hidden; }
  body {
    background: var(--canvas-bg);
    display: flex;
    align-items: center;
    justify-content: center;
  }
  .letterhead {
    position: relative;
    width: 800px;
    height: 1131px;
    background: var(--paper);
    box-shadow: 0 6px 24px rgba(0,0,0,0.12);
    overflow: hidden;
  }
  .letterhead__header {
    position: absolute;
    top: 60px;
    left: 60px;
    right: 60px;
    display: flex;
    align-items: center;
    justify-content: space-between;
  }
  .brand {
    display: flex;
    align-items: center;
    gap: 12px;
  }
  .brand__dot {
    width: 26px;
    height: 26px;
    border-radius: 50%;
    background: var(--brand-blue);
  }
  .brand__name {
    font-family: 'Montserrat', sans-serif;
    font-weight: 700;
    font-size: 30px;
    letter-spacing: 1px;
    color: var(--brand-blue);
  }
  .site-url {
    font-family: 'Montserrat', sans-serif;
    font-weight: 700;
    font-size: 12px;
    letter-spacing: 2px;
    color: var(--brand-blue);
  }
  .background-pattern {
    position: absolute;
    left: 0;
    right: 0;
    bottom: 0;
    height: 640px;
    background: linear-gradient(180deg, rgba(234,241,248,0) 0%, var(--pattern-soft) 45%, var(--pattern-mid) 100%);
  }
  .letter-body {
    position: absolute;
    top: 280px;
    left: 140px;
    width: 530px;
    font-family: 'Tinos', serif;
    font-size: 13.4px;
    line-height: 1.42;
    color: var(--text-dark);
    text-align: justify;
  }
  .letter-body p + p { margin-top: 17px; }
  .letterhead__footer {
    position: absolute;
    left: 140px;
    bottom: 52px;
    font-family: 'Montserrat', sans-serif;
    font-weight: 500;
    font-size: 8.5px;
    line-height: 1.45;
    color: var(--text-muted);
  }
  .signature {
    position: absolute;
    left: 450px;
    bottom: 70px;
    width: 170px;
    height: 60px;
    border-radius: 6px;
    background: linear-gradient(90deg, rgba(27,95,168,0.10), rgba(27,95,168,0.22), rgba(27,95,168,0.08));
  }
</style>
</head>
<body>
  <article class="letterhead">
    <div class="background-pattern" role="img" aria-label="Padrão decorativo suave em tons de azul claro no rodapé da folha"></div>

    <header class="letterhead__header">
      <div class="brand">
        <span class="brand__dot"></span>
        <span class="brand__name">AVECOM</span>
      </div>
      <span class="site-url">avecom.org.br</span>
    </header>

    <section class="letter-body">
      <p>Lorem ipsum dolor sit amet, consectetur adipiscing elit. Suspendisse sed odio arcu. Sed augue risus, pretium eget venenatis nec, posuere ut neque. Mauris elementum, nisl tincidunt tempus rutrum, nisl erat fringilla dui, ac facilisis neque massa cursus arcu. Integer vel lorem risus, eu tempus tellus. Etiam sit amet erat erat. Fusce eu orci velit, nec congue nunc. Etiam mollis rhoncus nisi, non tincidunt erat ultrices et. Vestibulum commodo erat eget quam semper pharetra. Pellentesque tempus dui non libero auctor sit amet interdum lorem volutpat. Fusce rutrum faucibus nulla, vel sodales urna vulputate et. Donec mi nulla, condimentum ac placerat non, bibendum et justo. Maecenas imperdiet augue sagittis nunc faucibus vel pellentesque quam tempus. Donec turpis dolor, viverra nec cursus ac, pulvinar et felis. Cum sociis natoque penatibus et magnis dis parturient montes, nascetur ridiculus mus. Vestibulum arcu eros, fringilla suscipit tempor sit amet, consequat ut nisi.</p>
      <p>Quisque scelerisque lobortis mi, id interdum neque varius ac. Sed tempor egestas nulla vel condimentum. Nullam lobortis eros non massa imperdiet porta. Fusce ornare euismod sem. Class aptent taciti sociosqu ad litora torquent per conubia nostra, per inceptos himenaeos. Etiam nec magna tortor. Aenean pretium vestibulum pulvinar. Pellentesque dui felis, scelerisque vitae euismod sit amet, scelerisque nec mi. Sed posuere nisl dictum nulla dapibus sodales. Proin tempor consequat tortor. In vulputate molestie arcu vitae ornare. Vivamus sed quam orci. Mauris neque justo, dictum id feugiat a, aliquet a orci. Donec elementum, libero et laoreet suscipit, nisi risus ornare elit, non sollicitudin nisi tortor sit amet tellus. Maecenas interdum lectus vitae neque adipiscing blandit. Donec eget libero orci, in condimentum nunc.</p>
      <p>Lorem risus, eu tempus tellus. Etiam sit amet erat erat. Fusce eu orci velit, nec congue nunc. Etiam mollis rhoncus nisi, non tincidunt erat ultrices et. Vestibulum commodo erat eget quam semper pharetra. Pellentesque tempus dui non libero auctor sit amet interdum lorem volutpat. Fusce rutrum faucibus nulla, vel sodales urna vulputate et. Donec mi nulla, condimentum ac placerat non, bibendum et justo. Maecenas imperdiet augue sagittis nunc faucibus vel pellentesque quam tempus. Donec turpis dolor, viverra nec cursus ac, pulvinar et felis.</p>
    </section>

    <div class="signature" role="img" aria-label="Assinatura manuscrita do responsável"></div>

    <footer class="letterhead__footer">
      R. das Araucárias, 148<br>
      Centro | Vale Claro<br>
      Paraná | Brasil<br>
      +55 (41) 3 5550-2040<br>
      contato@avecom.org.br
    </footer>
  </article>
</body>
</html>
```